Presentation for Design Industry

Halvorsen Custom Plastics & Acrylics is a custom plastic design/build company based in Canada that actively collaborates with Architects, Designers and Builders.
The versatility and economic attractiveness of plastics has engendered a renaissance in the use of this material in all aspects for our wide client base. We have changed our company from being a custom manufacturer. We are now embracing the opportunity to be part of the design process and contribute\ing unique design features using leading edge approaches and materials.
We would like our presentation to highlight this new design aspect of our company. One of our partners is www.vantelux-panels.example ~ this particular website outlines much of what we do and can be used as an example for design focussed towards our same target market. We are looking for a high-end, original presentation. If the design and concept is good, there are opportunities to be involved in our new website build within the next month.
A loose outline of our presentation is uploaded for your reference. Our brochures and graphics files are also available for your reference.
Adobe Acrobat Presentation*, PowerPoint or Google Presentation
http://halvorsenplastics.example/interior-industrial-design.htm
https://files.example.net/sh/bx4kw7rmt2n9cfa/Rpln52ke3q
Updates
Thank you to all who worked on submitting your designs based on a vague but necessary description. We were looking for something to pop out at us...not knowing exactly what we wanted we needed a design concept to emerge from the information we were able to provide. Perhaps this needed some entrepreneurial thought process or marketing experience behind the design concept. You all had great ideas. Thank you again for all your hard work and creativity!
Target Market(s)
Interior Designers; Architects; Environmental Designer, Building Contractors, Retail Designers
Industry/Entity Type
Plastic
Look and feel
Each slider illustrates characteristics of the customer's brand and the style your logo design should communicate.

```html
<!DOCTYPE html>
<html lang="en">
<head>
<meta charset="utf-8">
<title>Our Values – Halvorsen Custom Plastics &amp; Acrylics</title>
<link rel="stylesheet" href="https://fonts.googleapis.com/css2?family=Open+Sans:wght@400;600&display=swap">
<style>
  :root {
    --stage: #000000;
    --paper: #ffffff;
    --accent: #e2731c;
    --ink: #1a1a1a;
    --brand-ink: #1d3a5c;
    --photo-red: #c8202a;
    --photo-deep: #8e1219;
    --photo-grey: #cfd3d6;
    --photo-light: #eef0f1;
  }
  * { margin: 0; padding: 0; box-sizing: border-box; }
  html, body { width: 1200px; height: 711px; overflow: hidden; background: var(--stage); }
  .slide {
    position: absolute; left: 150px; top: 18px;
    width: 900px; height: 675px;
    background: var(--paper);
    font-family: "Open Sans", sans-serif;
    overflow: hidden;
  }
  .slide-photo {
    position: absolute; left: 0; top: 239px; width: 900px; height: 436px;
    background:
      radial-gradient(ellipse 40% 55% at 35% 70%, var(--photo-red), transparent 70%),
      radial-gradient(ellipse 30% 40% at 60% 85%, var(--photo-deep), transparent 70%),
      radial-gradient(ellipse 25% 50% at 90% 40%, var(--photo-red), transparent 70%),
      linear-gradient(100deg, var(--photo-light) 0%, var(--photo-grey) 25%, #b7453f 45%, var(--photo-red) 65%, #a8b0b6 90%);
  }
  .slide-title {
    position: absolute; left: 38px; top: 72px;
    font-size: 47px; font-weight: 400; color: var(--accent);
    letter-spacing: 0.5px; line-height: 1;
  }
  .values-panel {
    position: absolute; left: 359px; top: 90px;
    width: 470px; height: 443px;
    background: var(--paper);
  }
  .values-list { list-style: none; padding: 12px 0 0 42px; }
  .values-list li {
    position: relative;
    font-size: 28px; line-height: 35px; color: var(--ink);
    margin-bottom: 10px; padding-right: 20px;
  }
  .values-list li::before {
    content: ""; position: absolute; left: -31px; top: 14px;
    width: 7px; height: 8px; background: var(--accent);
  }
  .brand-tag {
    position: absolute; left: 363px; top: 618px;
    width: 142px; height: 57px; background: var(--paper);
    display: flex; align-items: center; justify-content: center; gap: 6px;
  }
  .brand-mark { width: 12px; height: 12px; background: var(--brand-ink); }
  .brand-name {
    font-size: 17px; font-weight: 600; color: var(--brand-ink); letter-spacing: 0.3px;
  }
</style>
</head>
<body>
  <main class="slide">
    <div class="slide-photo" role="img" aria-label="Close-up photograph of curved red and white acrylic sheets being heat-formed"></div>
    <h1 class="slide-title">Our Values</h1>
    <section class="values-panel">
      <ul class="values-list">
        <li>Appreciate and share profits with employees.</li>
        <li>Quality as a result of continuous improvement (get a little better every day).</li>
        <li>Professionalism and integrity in everything we do.</li>
        <li>Guard our reputation ruthlessly.Text</li>
      </ul>
    </section>
    <div class="brand-tag" aria-label="Halvorsen Custom Plastics &amp; Acrylics">
      <span class="brand-mark"></span>
      <span class="brand-name">HALVORSEN</span>
    </div>
  </main>
</body>
</html>
```